Professional services business card

This is for a new business in New Zealand, providing professional advice to boards of directors of companies
The point of difference is a strong blend of Financial and IT knowledge

Target audience are senior business executives, CEO/CFO/President, etc.
So, simple but appealing
Business colours are orange and blue

Sample logo attached
proposed Content also attached - feedback on wording is welcome
Updates

Please provide for a logo to be added - about 30 mm wide and 10 mm high

the company name is "Korvale Meridian Ltd" - logo now uploaded to the project brief

Information to include are now in the second file that was uploaded

Industry/Entity Type

Business

```html
<!DOCTYPE html>
<html lang="en">
<head>
<meta charset="utf-8">
<title>Korvale Meridian Ltd – Business Card</title>
<link rel="stylesheet" href="https://fonts.googleapis.com/css2?family=Nunito:wght@800&family=Open+Sans:wght@400;600;700&family=Lora:ital,wght@1,700&display=swap">
<style>
  :root {
    --brand-blue: #2a9ad6;
    --brand-blue-light: #58b9ea;
    --brand-orange: #f28c1c;
    --card-white: #ffffff;
    --text-white: #ffffff;
    --backdrop: #e4e2dd;
  }
  * { box-sizing: border-box; margin: 0; padding: 0; }
  html, body {
    width: 1200px; height: 780px; overflow: hidden;
    background: var(--backdrop);
    font-family: "Open Sans", Arial, sans-serif;
  }
  .canvas {
    width: 1200px; height: 780px;
    display: flex; align-items: center; justify-content: center; gap: 40px;
  }
  .card {
    position: relative;
    width: 540px; height: 324px;
    border-radius: 26px;
    overflow: hidden;
    box-shadow: 0 6px 18px rgba(0,0,0,0.18);
  }

  /* Back side */
  .card-back {
    background: var(--brand-blue);
    color: var(--text-white);
    text-align: center;
    padding-top: 34px;
  }
  .card-back .brand-name {
    font-family: "Nunito", "Open Sans", sans-serif;
    font-weight: 800;
    font-size: 40px;
    line-height: 1;
    color: var(--brand-blue-light);
    letter-spacing: 0.5px;
  }
  .card-back .tagline {
    font-family: "Lora", Georgia, serif;
    font-style: italic;
    font-weight: 700;
    font-size: 19px;
    margin-top: 26px;
  }
  .card-back .divider {
    width: 300px; height: 2px;
    margin: 6px auto 14px;
    background: linear-gradient(90deg, var(--text-white), var(--brand-orange));
  }
  .services {
    list-style: none;
    display: inline-block;
    text-align: left;
    font-weight: 700;
    font-size: 15px;
    line-height: 25px;
    letter-spacing: 0.4px;
  }
  .services li::before {
    content: "";
    display: inline-block;
    width: 8px; height: 8px;
    border-radius: 50%;
    background: var(--brand-orange);
    margin-right: 9px;
    vertical-align: 2px;
  }

  /* Front side */
  .card-front { background: var(--card-white); }
  .front-top {
    height: 162px;
    position: relative;
  }
  .front-logo {
    position: absolute; left: 34px; top: 44px;
    display: flex; align-items: center; gap: 10px;
  }
  .front-logo .mark-dot {
    width: 18px; height: 18px; border-radius: 50%;
    background: var(--brand-orange);
  }
  .front-logo .brand-name {
    font-family: "Nunito", "Open Sans", sans-serif;
    font-weight: 800;
    font-size: 38px;
    line-height: 1;
    color: var(--brand-blue);
  }
  .person {
    position: absolute; right: 34px; bottom: 22px;
    text-align: right;
  }
  .person-name {
    font-weight: 700; font-size: 17px; color: var(--brand-blue);
  }
  .person-credentials {
    font-size: 9.5px; color: var(--brand-orange); letter-spacing: 0.2px;
  }
  .front-bottom {
    position: absolute; left: 0; right: 0; bottom: 0;
    height: 162px;
    background: var(--brand-blue);
    padding: 20px 0 0 34px;
    overflow: hidden;
  }
  .contact-list { list-style: none; color: var(--text-white); font-size: 15px; }
  .contact-list li { display: flex; align-items: center; gap: 9px; height: 27px; }
  .contact-list svg { width: 15px; height: 15px; flex: none; fill: var(--brand-orange); }
  .corner-accent {
    position: absolute; right: -30px; bottom: -30px;
    width: 150px; height: 150px; border-radius: 50%;
    background: var(--brand-blue-light); opacity: 0.35;
  }
</style>
</head>
<body>
<main class="canvas">

  <section class="card card-back" aria-label="Card back">
    <div class="brand-name">Korvale Meridian</div>
    <p class="tagline">Talk to us about</p>
    <div class="divider"></div>
    <ul class="services">
      <li>Governance</li>
      <li>Good Practice</li>
      <li>Financial Strategy</li>
      <li>Information Technology</li>
      <li>Mentoring</li>
    </ul>
  </section>

  <section class="card card-front" aria-label="Card front">
    <div class="front-top">
      <div class="front-logo">
        <span class="mark-dot"></span>
        <span class="brand-name">Korvale Meridian</span>
      </div>
      <div class="person">
        <div class="person-name">Tamsin Rowe</div>
        <div class="person-credentials">M.Com, ACA(NZ), ACMA</div>
      </div>
    </div>
    <div class="front-bottom">
      <div class="corner-accent"></div>
      <ul class="contact-list">
        <li>
          <svg viewBox="0 0 16 16" aria-hidden="true"><path d="M3 1h3l1.5 4-2 1.3a9 9 0 0 0 4.2 4.2L11 8.5l4 1.5v3a2 2 0 0 1-2 2A12 12 0 0 1 1 3a2 2 0 0 1 2-2z"/></svg>
          021 555 0187
        </li>
        <li>
          <svg viewBox="0 0 16 16" aria-hidden="true"><path d="M1 3h14v10H1z" /><path d="M1 3l7 6 7-6" fill="none" stroke="#2a9ad6" stroke-width="1.4"/></svg>
          Tamsin.Rowe@korvale.co.nz
        </li>
        <li>
          <svg viewBox="0 0 16 16" aria-hidden="true"><path d="M8 0a5.5 5.5 0 0 1 5.5 5.5C13.5 10 8 16 8 16S2.5 10 2.5 5.5A5.5 5.5 0 0 1 8 0zm0 3.3a2.2 2.2 0 1 0 0 4.4 2.2 2.2 0 0 0 0-4.4z"/></svg>
          2741, Harbour Lane, Wellington, 5010
        </li>
        <li>
          <svg viewBox="0 0 16 16" aria-hidden="true"><rect x="1" y="1" width="14" height="14" rx="2"/></svg>
          profiles.korvale.co.nz/tamsinrowe
        </li>
      </ul>
    </div>
  </section>

</main>
</body>
</html>
```